Briefpapier für Träger der Familienhilfe
Sie geht auf alle Wünsche sehr schnell ein!! Sehr gute Zusammenarbeit! Danke
Zielgruppe
Wir sind ein Träger der Familienhilfe und bieten Hilfen zur Erziehung an. Unsere Auftraggeber sind die Jugendämter in Hamburg. Unsere Zielgruppe sind Familien/Einzelpersonen in Krisensituationen.
Aufgabenstellung
Wir möchten, dass unser Logo in das Design integriert wird. Da der Briefverkehr hauptsächlich mit Behörden, Ämtern, Schulen etc. stattfinden wird, ist es wichtig, dass wir einen seriösen Eindruck machen.

```html
<!DOCTYPE html>
<html lang="de">
<head>
<meta charset="utf-8">
<title>Briefpapier Lumo Familienhilfe</title>
<link href="https://fonts.googleapis.com/css2?family=Montserrat:wght@400;500;700&family=Didact+Gothic&display=swap" rel="stylesheet">
<style>
  :root {
    --green: #8dc63f;
    --grey: #8e8e8e;
    --dark: #3a3a3a;
    --backdrop: #9d9d9d;
    --paper: #ffffff;
  }
  html, body { margin: 0; padding: 0; overflow: hidden; }
  body {
    width: 989px; height: 1200px;
    background: var(--backdrop);
    position: relative;
    font-family: "Montserrat", sans-serif;
  }
  .sheet {
    position: absolute; left: 84px; top: 20px;
    width: 820px; height: 1160px;
    background: var(--paper);
    overflow: hidden;
  }
  .top-band { position: absolute; left: 0; top: 0; width: 100%; height: 10px; background: var(--green); }
  .brand { position: absolute; left: 34px; top: 58px; display: flex; align-items: center; gap: 12px; }
  .brand-dot { width: 34px; height: 34px; border-radius: 50%; background: var(--green); }
  .brand-name { font-family: "Montserrat", sans-serif; font-weight: 500; font-size: 30px; color: var(--grey); letter-spacing: 0.5px; }
  .sender-line { position: absolute; left: 35px; top: 155px; font-size: 11px; font-weight: 700; color: var(--dark); }
  .header-divider { position: absolute; left: 516px; top: 23px; width: 1.5px; height: 142px; background: #9a9a9a; }
  .contact { position: absolute; left: 545px; top: 34px; font-family: "Didact Gothic", sans-serif; font-size: 13px; color: var(--dark); line-height: 16px; }
  .contact-row { display: flex; align-items: flex-start; gap: 10px; margin-bottom: 10px; }
  .contact-row svg { flex: none; margin-top: 2px; }
  .footer-info { position: absolute; left: 0; top: 1077px; width: 100%; font-size: 11px; color: var(--dark); line-height: 20px; }
  .footer-col { position: absolute; top: 10px; }
  .footer-col.tax { left: 36px; }
  .footer-col.bank { left: 142px; top: 6px; }
  .footer-col.iban { left: 332px; top: 4px; line-height: 26px; }
  .footer-divider { position: absolute; top: 0; width: 1.5px; height: 50px; background: #9a9a9a; }
  .footer-bar { position: absolute; left: 0; bottom: 0; width: 820px; height: 80px; }
  .footer-url { position: absolute; right: 26px; bottom: 41px; font-size: 14px; font-weight: 700; color: #fff; }
</style>
</head>
<body>
  <div class="sheet">
    <div class="top-band"></div>

    <div class="brand">
      <div class="brand-dot"></div>
      <div class="brand-name">Lumo Familienhilfe</div>
    </div>
    <div class="sender-line">Kerstin Albers Beratung / Lindenweg 12 / D-22301 Hamburg</div>

    <div class="header-divider"></div>
    <div class="contact">
      <div class="contact-row">
        <svg width="24" height="24" viewBox="0 0 24 24"><circle cx="12" cy="12" r="11" fill="none" stroke="var(--grey)" stroke-width="1.5"/><path d="M8.5 7c1 0 1.5 2 1.5 2.5S9 11 9 11c.6 1.6 2.4 3.4 4 4 0 0 .9-1 1.5-1s2.5.5 2.5 1.5-1 1.8-2 1.8C10.5 17.3 6.7 13.5 6.7 9c0-1 .8-2 1.8-2z" fill="var(--green)"/></svg>
        <div>+49 40 5550 1284<br>+49 40 5550 1284</div>
      </div>
      <div class="contact-row">
        <svg width="24" height="24" viewBox="0 0 24 24"><circle cx="12" cy="12" r="11" fill="none" stroke="var(--grey)" stroke-width="1.5"/><path d="M12 5.5a4 4 0 0 0-4 4c0 3 4 8 4 8s4-5 4-8a4 4 0 0 0-4-4zm0 5.6a1.6 1.6 0 1 1 0-3.2 1.6 1.6 0 0 1 0 3.2z" fill="var(--green)"/></svg>
        <div>17, Harbor Plaza,<br>22 Boston, MA 02110</div>
      </div>
      <div class="contact-row">
        <svg width="24" height="24" viewBox="0 0 24 24"><circle cx="12" cy="12" r="11" fill="none" stroke="var(--grey)" stroke-width="1.5"/><circle cx="12" cy="12" r="6" fill="none" stroke="var(--green)" stroke-width="1.5"/><path d="M6 12h12M12 6c-2.5 3-2.5 9 0 12M12 6c2.5 3 2.5 9 0 12" fill="none" stroke="var(--green)" stroke-width="1.2"/></svg>
        <div>info@lumo-hilfe.de<br>www.lumo-hilfe.de</div>
      </div>
    </div>

    <div class="footer-info">
      <div class="footer-col tax">Steuer-Nr.<br>DE128450736</div>
      <div class="footer-divider" style="left:130px"></div>
      <div class="footer-col bank">Bankverbindung:<br>Stadtbank Nordhafen</div>
      <div class="footer-divider" style="left:318px"></div>
      <div class="footer-col iban">BIC NORDDEH1XXX<br>IBAN DE47 2105 0300 0004 3318 52</div>
    </div>

    <svg class="footer-bar" viewBox="0 0 820 80" aria-hidden="true">
      <rect x="0" y="47" width="820" height="33" fill="var(--green)"/>
      <path d="M548 23 H820 V49 H602 Q570 49 548 23 Z" fill="var(--grey)"/>
      <path d="M536 23 Q560 56 604 56 H820" fill="none" stroke="#fff" stroke-width="5"/>
    </svg>
    <div class="footer-url">www.albersberatung.de</div>
  </div>
</body>
</html>
```